Stationery Design Project

We need a stationery design for our Norwegian trucking company. We have existed for about 15 years and our 12 drivers uses relatively new vehicles to transport goods around in northern Norway. Long distance routes with fresh fish og food transport is our main operations.

We have already made alogo that's printed on our trucks. The logo and a picture of our trucks is attached. I think the logo i crappy, but since its already in use, changing it is not an option in this round. Still using a better colour scheme in the overall stationery and more interesting fonts is possible (altso in the logo).

Company details:
Name: Vikmarka AS
Organisation nr 983 517 608
Post adress: 8640 Brekka

I like minimalism and simplicity. I am avalibly for questions in normal GMT working hours either here or on mail: kjell@brekkafrakt.no

Reason: Hi. Im extending the deadline because I needed some time to find a vector file of our logo. Sorry for the inconvenience

Hi, and thanks for all your interest in the project. Some updates:

-          I have decided to commit to using one of the designs. Some designer will get the payment.

-          I have extended the deadline with 24 hours since I needed some time to find our firms vector logo (a slow Swedish man was holding me up)

-          We will not choose a design before the deadline. No need to rush.

-          We have received a lot of great design and think there is a need to specified the product we want to make:

o   Business Card for all our employers. I just need the design and will duplicate with the correct numbers and name myself. The information on should be: Logo, employer’s name, Phone number, email, website, Postal number and address. Use this as a template: logo, Leif Dahlberg, 47382950, Leif@brekkafrakt.no,, brekkafrakt.no, 8640 Brekka. The order and placement of the information is your creative decision.

o   Stickers to put on the goods we travel. On the sticker the should be the following information: Logo, phone number, Tekst and link: Fraktæ av Vikmarka. Ke du syns? Brekkafrakt.no/tilbakemelding (this means: Handled by Vikmarka. What do you think Brekkafrakt.no/feedback -à the link will be a feedback form). The placement the information and size is your creative decision with some stings: we have been thinking of using Prentolo for printing and see that a size about 6x6 cm, 8x5 or something like that. (with 3000 copies our budget is 200 punds). Any suggestions of other suppliers are welcome. Prentolo price calculator http://www.prentoloprints.example/digital-litho-printing/printing-labels-tags/stickers/

o   Letterhead with logo, address, phone number and organizational number.

o   Envelopes with logo,address, phone number and organizational number.

Have a nice day.

 

 

• Using the blue colour in the logo and using a similar graphic approch.

```html
<!DOCTYPE html>
<html lang="no">
<head>
<meta charset="utf-8">
<title>Vikmarka AS – stationery</title>
<link href="https://fonts.googleapis.com/css2?family=Source+Sans+3:wght@400;600;700&family=Great+Vibes&display=swap" rel="stylesheet">
<style>
  :root{
    --navy:#0d2a7a;
    --blue:#1a76d2;
    --ink:#555a60;
    --ink-dark:#333;
    --paper:#ffffff;
    --bg:#e9eaeb;
    --accent-fill:linear-gradient(135deg,var(--blue) 0%,var(--navy) 100%);
  }
  html,body{margin:0;padding:0;overflow:hidden}
  body{width:1200px;height:903px;position:relative;
    background:radial-gradient(ellipse at 50% 40%,#f6f6f6 0%,var(--bg) 70%,#d9dadb 100%);
    font-family:"Source Sans 3",Arial,sans-serif;color:var(--ink)}
  .sheet{position:absolute;background:var(--paper);box-shadow:0 2px 8px rgba(0,0,0,.25);overflow:hidden}
  .accent-area{position:absolute;background:var(--accent-fill)}
  .brand{position:absolute;display:flex;align-items:center;gap:8px;
    font-weight:600;color:var(--navy);letter-spacing:.2px;white-space:nowrap}
  .brand-dot{border-radius:50%;background:var(--blue)}
  .contact{position:absolute;border-left:1.5px solid var(--navy);color:var(--ink-dark)}
  .contact .firm{display:block}
  .contact .row{display:flex;align-items:center;gap:5px}
  .icon{fill:var(--navy);flex:none}

  /* letterhead */
  .letterhead{left:291px;top:12px;width:618px;height:876px}
  .letterhead .brand{left:40px;top:68px;font-size:34px}
  .letterhead .brand-dot{width:16px;height:16px}
  .letterhead .contact{left:466px;top:50px;height:62px;padding-left:15px}
  .letterhead .firm{font-size:12.5px;margin:-1px 0 6px}
  .letterhead .row{font-size:9.5px;line-height:14.5px}
  .letterhead .accent-area{right:0;bottom:0;width:160px;height:170px}
  .letter{position:absolute;left:73px;top:212px;width:498px;font-size:12px;line-height:16.5px}
  .letter .greeting{font-weight:700;color:var(--ink);margin:0 0 18px}
  .letter p{margin:0 0 16.5px}
  .signature{position:absolute;left:75px;top:660px;font-family:"Great Vibes",cursive;font-size:32px;color:var(--ink-dark);line-height:1}
  .role{position:absolute;left:75px;top:704px;font-size:12px;font-weight:700;color:var(--ink)}

  /* envelope */
  .envelope{left:522px;top:376px;width:650px;height:325px}
  .envelope .brand{left:32px;top:40px;font-size:25px}
  .envelope .brand-dot{width:12px;height:12px}
  .envelope .contact{left:246px;top:32px;height:48px;padding-left:12px}
  .envelope .firm{font-size:10px;margin:-1px 0 4px}
  .envelope .row{font-size:7.5px;line-height:11.5px}
  .envelope .accent-area{right:0;bottom:0;width:340px;height:40px}

  /* business cards */
  .card{width:266px;height:147px}
  .card-front{left:52px;top:376px}
  .card-front .accent-area{left:0;top:0;width:52px;height:147px}
  .card-front .brand{left:70px;top:58px;font-size:20px}
  .card-front .brand-dot{width:10px;height:10px}
  .card-back{left:52px;top:574px}
  .card-back .accent-area{right:0;top:0;width:62px;height:147px}
  .card-back .brand{left:10px;top:18px;font-size:15px}
  .card-back .brand-dot{width:8px;height:8px}
  .holder{position:absolute;left:17px;top:84px;width:158px;font-size:11px;color:var(--ink-dark);
    padding-bottom:4px;border-bottom:1px solid #8fa6cf}
  .card-contacts{position:absolute;left:17px;top:113px;display:grid;grid-template-columns:95px 80px;row-gap:2px;
    font-size:7px;color:var(--ink-dark)}
  .card-contacts .row{display:flex;align-items:center;gap:4px}

  /* sticker */
  .sticker{position:absolute;left:945px;top:85px;width:178px;height:178px;border-radius:50%;
    background:var(--paper);border:3px solid var(--navy);box-shadow:0 2px 8px rgba(0,0,0,.25);overflow:hidden;text-align:center}
  .sticker .intro{position:absolute;top:21px;left:0;right:0;font-size:11px;color:var(--ink-dark)}
  .sticker .brand{left:40px;top:46px;font-size:19px}
  .sticker .brand-dot{width:9px;height:9px}
  .sticker .question{position:absolute;top:92px;left:0;right:0;font-size:12px;color:var(--ink-dark);letter-spacing:.3px}
  .sticker .link-bar{position:absolute;top:110px;left:0;right:0;height:15px;background:var(--navy);color:#fff;font-size:10.5px;line-height:15px}
  .sticker .phone-bar{position:absolute;top:145px;left:48px;width:84px;height:11px;background:var(--blue);color:#fff;font-size:9px;line-height:11px;
    display:flex;align-items:center;justify-content:center;gap:4px}
  .sticker .phone-bar .icon{fill:#fff}
</style>
</head>
<body>

<svg width="0" height="0" style="position:absolute" aria-hidden="true">
  <symbol id="i-phone" viewBox="0 0 10 10"><rect x="1.5" y="0.5" width="7" height="9" rx="1"/><rect x="3" y="2" width="4" height="4" fill="#fff"/></symbol>
  <symbol id="i-pin" viewBox="0 0 10 10"><path d="M5 0.5a3.3 3.3 0 0 0-3.3 3.3C1.7 6.3 5 9.5 5 9.5s3.3-3.2 3.3-5.7A3.3 3.3 0 0 0 5 .5zm0 4.7a1.3 1.3 0 1 1 0-2.6 1.3 1.3 0 0 1 0 2.6z"/></symbol>
  <symbol id="i-web" viewBox="0 0 10 10"><circle cx="5" cy="5" r="4.5"/><path d="M3 3.5l2 1 1.5-1.5 .5 3-2 1.5-1-1.5z" fill="#fff"/></symbol>
  <symbol id="i-mail" viewBox="0 0 10 10"><rect x="0.5" y="2" width="9" height="6.5" rx=".6"/><path d="M1 2.5l4 3 4-3" fill="none" stroke="#fff" stroke-width=".9"/></symbol>
</svg>

<!-- Letterhead -->
<section class="sheet letterhead">
  <div class="brand"><span class="brand-dot"></span>Vikmarka</div>
  <div class="contact">
    <span class="firm">Vikmarka AS</span>
    <div class="row"><svg class="icon" width="9" height="9"><use href="#i-phone"/></svg>983 517 608</div>
    <div class="row"><svg class="icon" width="9" height="9"><use href="#i-pin"/></svg>8640 Brekka</div>
    <div class="row"><svg class="icon" width="9" height="9"><use href="#i-web"/></svg>www.brekkafrakt.no</div>
  </div>
  <div class="letter">
    <p class="greeting">Lorem Ipsum,</p>
    <p>Cras mattis consectetur purus sit amet fermentum. Etiam porta sem malesuada magna mollis euismod. Integer posuere erat a ante venenatis dapibus posuere velit aliquet. Cras justo odio, dapibus ac facilisis in, egestas eget quam. Aenean eu leo quam. Pellentesque ornare sem lacinia quam venenatis vestibulum.</p>
    <p>Vivamus sagittis lacus vel augue laoreet rutrum faucibus dolor auctor. Donec sed odio dui. Etiam porta sem malesuada magna mollis euismod. Morbi leo risus, porta ac consectetur ac, vestibulum at eros. Nullam id dolor id nibh ultricies vehicula ut id elit.</p>
    <p>Donec id elit non mi porta gravida at eget metus. Fusce dapibus, tellus ac cursus commodo, tortor mauris condimentum nibh, ut fermentum massa justo sit amet risus. Cras justo odio, dapibus ac facilisis in, egestas eget quam. Cum sociis natoque penatibus et magnis dis parturient montes, nascetur ridiculus mus.</p>
    <p>Cum sociis natoque penatibus et magnis dis parturient montes, nascetur ridiculus mus. Maecenas blandit tempus porttitor. Aenean lacinia bibendum nulla sed consectetur. Lorem ipsum dolor sit amet, consectetur adipiscing elit.</p>
    <p>Cras justo odio, dapibus ac facilisis in, egestas eget quam. Morbi leo risus, porta ac consectetur ac, vestibulum at eros. Duis mollis, est non commodo luctus, nisi erat porttitor ligula. Cras justo odio sem nec elit. Integer posuere erat a ante venenatis dapibus posuere velit aliquet. Vivamus sagittis lacus vel augue laoreet rutrum faucibus.</p>
  </div>
  <div class="signature">Your Name</div>
  <div class="role">Company Director</div>
  <div class="accent-area" role="img" aria-label="Decorative blue and navy corner accent"></div>
</section>

<!-- Envelope -->
<section class="sheet envelope">
  <div class="brand"><span class="brand-dot"></span>Vikmarka</div>
  <div class="contact">
    <span class="firm">Vikmarka AS</span>
    <div class="row"><svg class="icon" width="7" height="7"><use href="#i-phone"/></svg>983 517 608</div>
    <div class="row"><svg class="icon" width="7" height="7"><use href="#i-pin"/></svg>8640 Brekka</div>
    <div class="row"><svg class="icon" width="7" height="7"><use href="#i-web"/></svg>www.brekkafrakt.no</div>
  </div>
  <div class="accent-area" role="img" aria-label="Decorative blue and navy bottom accent"></div>
</section>

<!-- Business card front -->
<section class="sheet card card-front">
  <div class="accent-area" role="img" aria-label="Decorative blue and navy side accent"></div>
  <div class="brand"><span class="brand-dot"></span>Vikmarka</div>
</section>

<!-- Business card back -->
<section class="sheet card card-back">
  <div class="accent-area" role="img" aria-label="Decorative blue and navy side accent"></div>
  <div class="brand"><span class="brand-dot"></span>Vikmarka</div>
  <div class="holder">Leif Dahlberg</div>
  <div class="card-contacts">
    <div class="row"><svg class="icon" width="6" height="6"><use href="#i-phone"/></svg>47382950</div>
    <div class="row"><svg class="icon" width="6" height="6"><use href="#i-pin"/></svg>8640 Brekka</div>
    <div class="row"><svg class="icon" width="6" height="6"><use href="#i-mail"/></svg>Leif@brekkafrakt.no</div>
    <div class="row"><svg class="icon" width="6" height="6"><use href="#i-web"/></svg>brekkafrakt.no</div>
  </div>
</section>

<!-- Parcel sticker -->
<section class="sticker">
  <div class="intro">Fraktæ av</div>
  <div class="brand"><span class="brand-dot"></span>Vikmarka</div>
  <div class="question">KE DU SYNS?</div>
  <div class="link-bar">Brekkafrakt.no/tilbakemelding</div>
  <div class="phone-bar"><svg class="icon" width="7" height="7"><use href="#i-phone"/></svg>983 517 608</div>
</section>

</body>
</html>
```